Owen Tasker Studios Business Card

Looking for a clear, modern, elegant, sharp business card that conveys a professional yet edgy image to my business as a wedding, portrait, and travel photographer. Would like something that looks vintage yet modern. Need a new business card to grow my business. We are growing the business for Wedding and Event Photography as well as fine art Photography. (Mostly Landscapes)
Updates

I’m looking through designs now but I have a new logo that i want using please.

New logo uploaded please redesign using that

PLEASE ALL DESIGNERS LOOK IN BRIEF FOR NEW LOGO

Target Market(s)

Brides, Grooms, Families with Kids, People looking for Fine Art Photography Artwork

Industry/Entity Type

Photographer

Contact Information for Business Card

Unsure

Font styles to use
Serif

Colors

Designer to choose colors to be used in the design.

Requirements
Must have
• My Website:
• http://taskerlens.examplefolio.net
• Phone:
• 323-481-5206
• Email:
• owentaskerlens@mailbox-example.net
Nice to have
• Would like a sort of shine on the printing finish.
• I like black I think it looks good on a business card.
• Can try working with my logo (png that I've attached)

```html
<!DOCTYPE html>
<html lang="en">
<head>
<meta charset="utf-8">
<title>Owen Tasker Studios Business Card</title>
<link rel="stylesheet" href="https://fonts.googleapis.com/css2?family=Questrial&display=swap">
<style>
  :root {
    --backdrop: #3a3a3a;
    --card-dark: #0d0d0d;
    --card-mid: #262626;
    --ink: #f2f2f2;
    --ink-soft: #d9d9d9;
  }
  * { margin: 0; padding: 0; box-sizing: border-box; }
  html, body {
    width: 799px;
    height: 1200px;
    overflow: hidden;
    background: var(--backdrop);
    font-family: "Questrial", "Century Gothic", sans-serif;
  }
  .sheet {
    width: 799px;
    height: 1200px;
    display: flex;
    flex-direction: column;
    justify-content: space-around;
    align-items: center;
    padding: 40px 0;
  }
  .card {
    width: 630px;
    height: 360px;
    border-radius: 26px;
    background:
      linear-gradient(135deg, rgba(255,255,255,0.05) 0%, rgba(255,255,255,0.12) 45%, rgba(255,255,255,0.02) 80%),
      linear-gradient(180deg, var(--card-mid) 0%, var(--card-dark) 100%);
    box-shadow: 0 14px 30px rgba(0,0,0,0.55);
    color: var(--ink);
    display: flex;
    flex-direction: column;
    align-items: center;
    justify-content: center;
    text-align: center;
  }
  .brand {
    display: flex;
    flex-direction: column;
    align-items: center;
  }
  .brand-square {
    width: 62px;
    height: 62px;
    border: 2px solid var(--ink);
    margin-bottom: 14px;
  }
  .brand-name {
    font-size: 40px;
    letter-spacing: 1px;
    line-height: 1;
    text-transform: uppercase;
  }
  .brand-sub {
    font-size: 18px;
    letter-spacing: 14px;
    margin-top: 8px;
    padding-left: 14px;
    text-transform: uppercase;
  }
  .card-back .brand-square { width: 48px; height: 48px; margin-bottom: 10px; }
  .card-back .brand-name { font-size: 32px; }
  .card-back .brand-sub { font-size: 14px; letter-spacing: 11px; padding-left: 11px; }
  .contact {
    list-style: none;
    margin-top: 26px;
    font-size: 19px;
    line-height: 1.35;
    color: var(--ink-soft);
  }
</style>
</head>
<body>
<main class="sheet">
  <section class="card card-front" aria-label="Card front">
    <div class="brand">
      <div class="brand-square"></div>
      <div class="brand-name">Owen Tasker</div>
      <div class="brand-sub">Studios</div>
    </div>
  </section>

  <section class="card card-back" aria-label="Card back">
    <div class="brand">
      <div class="brand-square"></div>
      <div class="brand-name">Owen Tasker</div>
      <div class="brand-sub">Studios</div>
    </div>
    <ul class="contact">
      <li>323-481-5206</li>
      <li>owentaskerlens@mailbox-example.net</li>
      <li>www.taskerlens.examplefolio.net</li>
    </ul>
  </section>
</main>
</body>
</html>
```